A5 Certificate for a running Brisora Challenge

I would like a certificate designed called the "Brisora 50K Running Challenge"

It is presented to people that have run 50k in Brisora across 10 runs. So they have to run 10 runs with a minimum distance of 5K per run. This gives a total of 50k.

The certificate will need:

1. Map of Brisora in the background
2. Picture of a runner
3. Main title at the front to say "Brisora 50k Running Challenge"
4. Space to put the runners name on it. "Awarded to:"
5. Space to put the date the certificate is awarded. "Date Awarded:"

The design is then up to you but it needs to look official and professional. It is designed for teenagers so it needs to be "cool" and bold.

Any questions please ask.

Target Market(s)

Teenagers who want something cool and bold.

Font styles to use
Sans Serif

Colors
0556a4
fbee3f
33a6d7

Requirements
Must have
• 1. Map of Brisora in the background
• 2. Picture of a runner
• 3. Main title at the front to say "Brisora 50k Running Challenge"
• 4. Space to put the runners name on it. "Awarded to:"
• 5. Space to put the date the certificate is awarded. "Date Awarded:"
Nice to have
• Brisora is a sunny holiday location so it would be good to have sea blue colours and the sun in the design. to show the running challenge was done on a holiday island.

```html
<!DOCTYPE html>
<html lang="en">
<head>
<meta charset="utf-8">
<title>Brisora 50k Running Challenge Certificate</title>
<link rel="stylesheet" href="https://fonts.googleapis.com/css2?family=EB+Garamond:wght@500&family=Marcellus&family=Open+Sans:wght@400;500&family=Pinyon+Script&display=swap">
<style>
  :root {
    --page-bg: #e3e4e6;
    --card-bg: #ffffff;
    --ink-navy: #171647;
    --ink-muted: #4a4968;
    --frame-grey: #6d6d72;
    --rule-lilac: #a9a6c4;
    --map-peach: #f5b08c;
    --wave-blue: #5aa8e0;
    --wave-teal: #7fb9c9;
    --wave-orange: #f7892f;
    --wave-red: #ee3a26;
    --runner-navy: #2d2d6e;
    --mark-navy: #2a2660;
  }
  * { margin: 0; padding: 0; box-sizing: border-box; }
  html, body {
    width: 1200px; height: 1200px; overflow: hidden;
    background: var(--page-bg);
  }
  .certificate {
    position: absolute; left: 40px; top: 205px;
    width: 1120px; height: 790px;
    background: var(--card-bg);
    overflow: hidden;
  }
  .wave-band { position: absolute; pointer-events: none; }
  .wave-band--blue {
    left: 0; top: 180px; width: 560px; height: 300px;
    background: radial-gradient(ellipse 70% 45% at 15% 45%, rgba(90,168,224,.55), rgba(90,168,224,.15) 60%, transparent 80%);
  }
  .wave-band--teal {
    left: 420px; top: 200px; width: 480px; height: 260px;
    background: radial-gradient(ellipse 60% 35% at 55% 40%, rgba(127,185,201,.45), transparent 75%);
  }
  .wave-band--fire {
    right: 0; top: 170px; width: 520px; height: 340px;
    background: radial-gradient(ellipse 80% 45% at 95% 50%, rgba(238,58,38,.85), rgba(247,137,47,.55) 45%, rgba(247,137,47,.12) 70%, transparent 85%);
  }
  .island-map {
    position: absolute; left: 177px; top: 100px; width: 814px; height: 562px;
    background: radial-gradient(ellipse 50% 48% at 55% 48%, rgba(245,176,140,.85), rgba(245,176,140,.55) 60%, transparent 90%);
    border-radius: 46% 54% 40% 60% / 45% 40% 60% 55%;
  }
  .runner-figure {
    position: absolute; left: 705px; top: 214px; width: 262px; height: 276px;
    background: radial-gradient(ellipse 45% 50% at 55% 45%, rgba(45,45,110,.85), rgba(45,45,110,.45) 65%, transparent 90%);
    border-radius: 50%;
  }
  .frame {
    position: absolute; left: 35px; top: 41px; width: 1047px; height: 705px;
    border: 2px solid var(--frame-grey);
  }
  .region-mark {
    position: absolute; left: 555px; top: 78px; width: 44px; height: 34px;
    background: var(--mark-navy);
  }
  .title-region, .title-distance, .title-event {
    position: absolute; left: 0; width: 100%;
    text-align: center; color: var(--ink-navy); line-height: 1;
  }
  .title-region {
    top: 138px; padding-left: 26px;
    font-family: "Marcellus", serif;
    font-size: 60px; letter-spacing: 32px;
  }
  .title-distance {
    top: 198px; padding-left: 10px;
    font-family: "EB Garamond", serif; font-weight: 500;
    font-variant-numeric: lining-nums;
    font-size: 300px; letter-spacing: -6px;
  }
  .title-event {
    top: 485px; padding-left: 8px;
    font-family: "Marcellus", serif;
    font-size: 70px; letter-spacing: 8px;
  }
  .award-label {
    position: absolute; left: 178px; top: 616px;
    font-family: "Open Sans", sans-serif; font-weight: 500;
    font-size: 22px; color: var(--ink-navy);
  }
  .award-name {
    position: absolute; left: 405px; top: 578px;
    font-family: "Pinyon Script", cursive;
    font-size: 64px; color: var(--ink-navy); line-height: 1;
  }
  .award-rule {
    position: absolute; left: 345px; top: 629px; width: 597px; height: 2px;
    background: var(--rule-lilac);
  }
  .award-date {
    position: absolute; left: 0; width: 100%; top: 664px;
    text-align: center;
    font-family: "Open Sans", sans-serif; font-size: 22px;
    color: var(--ink-muted);
  }
</style>
</head>
<body>
  <main class="certificate">
    <div class="wave-band wave-band--blue" role="img" aria-label="Flowing blue sea-wave light streaks"></div>
    <div class="island-map" role="img" aria-label="Soft peach map of the island"></div>
    <div class="wave-band wave-band--teal" role="img" aria-label="Translucent teal ribbon streaks"></div>
    <div class="wave-band wave-band--fire" role="img" aria-label="Orange and red sunlit speed streaks"></div>
    <div class="runner-figure" role="img" aria-label="Silhouette of a running woman with flowing hair"></div>

    <div class="frame"></div>
    <div class="region-mark" role="img" aria-label="Regional emblem"></div>

    <h1 class="title-region">BRISORA</h1>
    <div class="title-distance">50k</div>
    <div class="title-event">RUNNING CHALLENGE</div>

    <div class="award-label">AWARDED TO:</div>
    <div class="award-name">Your Name</div>
    <div class="award-rule"></div>
    <div class="award-date">08-22-2019</div>
  </main>
</body>
</html>
```